SWPD (Street Wide Postal Drop) Mailer - Direct Mail Piece

We want to create a SWPD Mailer (Street Wide Postal Drop)
We are looking to create a new mailer to be sent to prospective new customers. We pinpoint these mailings to specific customers in the communities we are looking to grow our business. These are High End Communities. High Wealth Clients.

We have included some examples of other supporting items we have used in the past. PLEASE NOTE: We are NOT looking to promote the R & T Pool Plastering. That was a one time promotion. We are looking to focus on our company Tidewell and the services we offer. The current SWPD Mailer is 6 1/4 X 9 and that sample was attached.

Our goal is to get the customers to call us

561 TIDEWELL = 561-555-0148
844 TIDEWELL = 844-555-0148 (Toll Free)
www.tidewellservice.com
www.friendnet.com/TidewellFla

We Are Professional - Provide Fast Reliable Service and Repairs

We Offer:
Pool Service
Pool Repairs
Pool Equipment Repairs
Pool Remodeling
Pool Resurfacing
Pool Tile Installation or Repair
Pool Deck Installations
Pool Equipment Installation or Repair
Pool Leak Detection and Leak Repairs
Licensed and Insured

We send an e-mail after we service the pool showing what employee was there on what day and time and what was done. (GPS Date & Time Stamped) This includes Pictures of YOUR Pool! Our Customers Love This Feature! They know who was there, when they were there and what they did! This e-mail is sent before our Pool Technician leaves the customers home all in real time.

All Employees are tracked by GPS so we know were they are and how much time they spend at each clients home. All employees where company uniforms and drive company vehicles with proper logos, phone numbers and website address.

Please Ask any Questions. We want to make sure we are sending a clear message.

Thank You For Your Help!

Target Market(s)

High End Communities. High Wealth Clients.

Requirements
Must have
• Call To Action.
We Want Them To Pick Up The Phone and CALL US!

New Customers Get One Month FREE
Nice to have
• Professional Look and Feel - Clean and Professional

```html
<!DOCTYPE html>
<html lang="en">
<head>
<meta charset="utf-8">
<title>Tidewell – SWPD Mailer</title>
<link href="https://fonts.googleapis.com/css2?family=Montserrat:ital,wght@0,500;0,600;0,700;0,800;1,800&family=Mulish:ital,wght@0,400;0,700;1,400&family=Roboto+Condensed:wght@700&display=swap" rel="stylesheet">
<style>
  :root{
    --page:#e4e5e8;
    --sky:#2aa0e0;
    --sky-deep:#1787c9;
    --sky-light:#6fcdf5;
    --navy:#1b3a8a;
    --steel:#2a7bab;
    --orange:#f5a623;
    --gold:#f7b733;
    --white:#ffffff;
    --ink:#1e1e1e;
  }
  *{box-sizing:border-box;margin:0;padding:0}
  html,body{width:884px;height:1200px;overflow:hidden;background:var(--page)}
  body{position:relative;font-family:"Mulish",sans-serif;color:var(--ink)}
  .card{position:absolute;left:63px;width:757px;height:527px;background:var(--white);overflow:hidden;box-shadow:0 4px 10px rgba(0,0,0,.25)}
  .card--front{top:43px}
  .card--back{top:595px}
  .abs{position:absolute}

  /* front */
  .hero{left:0;top:0;width:757px;height:400px;background:linear-gradient(110deg,#4dc0f0 0%,#2aa3e3 45%,#229ade 100%)}
  .hero-photo{left:0;top:0;width:360px;height:360px;background:radial-gradient(circle at 55% 45%,#e8b9a8 0%,#7fc7ee 45%,rgba(42,163,227,0) 75%)}
  .recommend{left:386px;top:36px;font:700 19px/1 "Montserrat",sans-serif;color:var(--white);letter-spacing:.3px}
  .brand-big{left:384px;top:58px;font:800 43px/1 "Montserrat",sans-serif;color:var(--navy)}
  .service-title{left:386px;top:104px;font:700 30px/1 "Montserrat",sans-serif;color:var(--white)}
  .offer-list{list-style:none;font-size:12.5px;line-height:15.5px;color:var(--white)}
  .offer-list li{position:relative;padding-left:17px;margin-bottom:3px}
  .offer-list li svg{position:absolute;left:0;top:2px}
  .offers-a{left:389px;top:154px;width:168px}
  .offers-b{left:560px;top:154px;width:160px}
  .thumb{top:304px;width:113px;height:73px;border:4px solid var(--white);border-radius:4px;box-shadow:0 2px 4px rgba(0,0,0,.25)}
  .thumb-1{left:360px;background:linear-gradient(135deg,#4cb3d8,#2a7fa8)}
  .thumb-2{left:483px;background:linear-gradient(180deg,#c9a67a 0%,#8aa38a 55%,#3b9fd8 100%)}
  .thumb-3{left:606px;background:linear-gradient(120deg,#6b6f74,#cfd3d6 55%,#2f8ed0)}
  .front-wave{left:0;top:330px}
  .badge{left:217px;top:313px;width:86px;height:86px;border-radius:50%;background:var(--gold);border:2px solid var(--white);box-shadow:0 2px 5px rgba(0,0,0,.2);color:var(--white);text-align:center;font-family:"Montserrat",sans-serif;font-weight:800}
  .badge-text{position:absolute;left:0;right:0;top:19px;transform:rotate(-22deg)}
  .badge-text b{display:block;font-size:21px;line-height:20px}
  .badge-text span{display:block;font-size:10.5px;line-height:11px}
  .call-line{font:500 14px/1 "Montserrat",sans-serif;color:var(--ink);white-space:nowrap}
  .call-line strong{font-weight:700}
  .phone{font:800 27px/1 "Montserrat",sans-serif;color:var(--orange);white-space:nowrap}
  .web{font:700 15px/1 "Montserrat",sans-serif;white-space:nowrap}
  .social{font:500 11px/1 "Montserrat",sans-serif;color:var(--ink);white-space:nowrap}
  .front-call{left:32px;top:430px}
  .front-phone{left:31px;top:447px}
  .front-web{left:272px;top:441px;color:var(--steel)}
  .front-social{left:274px;top:461px}
  .promise-band{left:32px;top:483px;width:451px;height:20px;background:var(--steel);color:var(--white);font:400 11px/20px "Montserrat",sans-serif;padding-left:5px;white-space:nowrap;overflow:hidden}
  .promise-band strong{font-weight:700}
  .band-slash{left:481px;top:483px}
  .brandmark{display:flex;align-items:center;gap:8px;white-space:nowrap}
  .brandmark .dot{width:20px;height:20px;border-radius:50%;background:var(--gold);flex:none}
  .brandmark .name{font:800 34px/1 "Montserrat",sans-serif;color:var(--navy)}
  .front-brand{left:540px;top:440px}

  /* back */
  .back-brand{left:78px;top:62px}
  .back-brand .name{font-size:38px}
  .back-tagline{left:335px;top:96px;font:500 14px/15.5px "Montserrat",sans-serif;color:var(--orange)}
  .back-tagline strong{font-weight:700}
  .indicia{left:657px;top:32px;width:63px;height:50px;border:1px solid #333;font:400 7px/9.4px Arial,sans-serif;text-align:center;padding-top:2px}
  .address{left:585px;top:91px;width:136px;height:46px;border:1px solid #333;font:400 10px/12px Arial,sans-serif;padding:11px 0 0 11px}
  .diff-head{left:34px;top:170px;width:289px;height:23px;background:var(--steel);color:var(--white);font:700 15.5px/23px "Montserrat",sans-serif;padding-left:11px;white-space:nowrap}
  .diff-motto{left:323px;top:170px;width:260px;height:23px;border:1px solid #9fc3dc;font:600 9.6px/21px "Montserrat",sans-serif;padding-left:10px;white-space:nowrap}
  .diff-list{list-style:none;font-size:11.3px;line-height:14.5px;color:var(--ink)}
  .diff-list li{position:relative;padding-left:13px;margin-bottom:4px;white-space:nowrap}
  .diff-list li.bullet::before{content:"";position:absolute;left:0;top:5px;width:4px;height:4px;border-radius:50%;background:var(--sky-deep)}
  .diff-a{left:34px;top:208px;width:290px}
  .diff-b{left:332px;top:208px;width:300px}
  .back-wave{left:0;top:342px}
  .round-photo{left:544px;top:304px;width:176px;height:176px;border-radius:50%;border:3px solid var(--white);background:radial-gradient(circle at 40% 40%,#3d8ff0,#1a5fd0 70%);box-shadow:0 0 0 1px rgba(255,255,255,.6)}
  .ready{left:36px;top:400px;font:800 italic 19px/1 "Montserrat",sans-serif;color:var(--navy);white-space:nowrap}
  .look{left:36px;top:422px;font:400 italic 13.5px/1 "Mulish",sans-serif;color:var(--navy);white-space:nowrap}
  .ribbon{left:301px;top:390px}
  .ribbon-text{left:301px;top:394px;width:181px;text-align:center;font:700 15px/15px "Roboto Condensed",sans-serif;color:var(--white)}
  .back-call{left:36px;top:456px}
  .back-phone{left:35px;top:475px}
  .back-web{left:292px;top:470px;color:var(--white);font-size:16px}
  .back-social{left:295px;top:493px;color:var(--navy)}
  .licensed{left:537px;top:497px;font:700 12px/1 "Roboto Condensed",sans-serif;color:var(--navy);letter-spacing:.2px;white-space:nowrap}
</style>
</head>
<body>

<section class="card card--front">
  <div class="abs hero" role="img" aria-label="Underwater photo of a young swimmer in goggles giving a thumbs up in a blue pool"></div>
  <div class="abs hero-photo" aria-hidden="true"></div>

  <p class="abs recommend">WE RECOMMEND</p>
  <h1 class="abs brand-big">TIDEWELL</h1>
  <h2 class="abs service-title">POOL SERVICE</h2>

  <ul class="abs offer-list offers-a">
    <li><svg width="11" height="11" viewBox="0 0 11 11"><circle cx="5.5" cy="5.5" r="5.5" fill="#f5b428"/><path d="M2.8 5.6l1.8 1.8 3.6-3.8" stroke="#fff" stroke-width="1.4" fill="none"/></svg>Pool Service</li>
    <li><svg width="11" height="11" viewBox="0 0 11 11"><circle cx="5.5" cy="5.5" r="5.5" fill="#f5b428"/><path d="M2.8 5.6l1.8 1.8 3.6-3.8" stroke="#fff" stroke-width="1.4" fill="none"/></svg>Pool Repairs</li>
    <li><svg width="11" height="11" viewBox="0 0 11 11"><circle cx="5.5" cy="5.5" r="5.5" fill="#f5b428"/><path d="M2.8 5.6l1.8 1.8 3.6-3.8" stroke="#fff" stroke-width="1.4" fill="none"/></svg>Pool Equipment Repairs</li>
    <li><svg width="11" height="11" viewBox="0 0 11 11"><circle cx="5.5" cy="5.5" r="5.5" fill="#f5b428"/><path d="M2.8 5.6l1.8 1.8 3.6-3.8" stroke="#fff" stroke-width="1.4" fill="none"/></svg>Pool Remodeling</li>
    <li><svg width="11" height="11" viewBox="0 0 11 11"><circle cx="5.5" cy="5.5" r="5.5" fill="#f5b428"/><path d="M2.8 5.6l1.8 1.8 3.6-3.8" stroke="#fff" stroke-width="1.4" fill="none"/></svg>Pool Resurfacing</li>
    <li><svg width="11" height="11" viewBox="0 0 11 11"><circle cx="5.5" cy="5.5" r="5.5" fill="#f5b428"/><path d="M2.8 5.6l1.8 1.8 3.6-3.8" stroke="#fff" stroke-width="1.4" fill="none"/></svg>Pool Tile Installation or<br>Repair</li>
  </ul>
  <ul class="abs offer-list offers-b">
    <li><svg width="11" height="11" viewBox="0 0 11 11"><circle cx="5.5" cy="5.5" r="5.5" fill="#f5b428"/><path d="M2.8 5.6l1.8 1.8 3.6-3.8" stroke="#fff" stroke-width="1.4" fill="none"/></svg>Pool Deck Installations</li>
    <li><svg width="11" height="11" viewBox="0 0 11 11"><circle cx="5.5" cy="5.5" r="5.5" fill="#f5b428"/><path d="M2.8 5.6l1.8 1.8 3.6-3.8" stroke="#fff" stroke-width="1.4" fill="none"/></svg>Pool Equipment<br>Installation or Repair</li>
    <li><svg width="11" height="11" viewBox="0 0 11 11"><circle cx="5.5" cy="5.5" r="5.5" fill="#f5b428"/><path d="M2.8 5.6l1.8 1.8 3.6-3.8" stroke="#fff" stroke-width="1.4" fill="none"/></svg>Pool Leak Detection<br>and Leak Repairs</li>
    <li><svg width="11" height="11" viewBox="0 0 11 11"><circle cx="5.5" cy="5.5" r="5.5" fill="#f5b428"/><path d="M2.8 5.6l1.8 1.8 3.6-3.8" stroke="#fff" stroke-width="1.4" fill="none"/></svg>Licensed and Insured</li>
  </ul>

  <svg class="abs front-wave" width="757" height="197" viewBox="0 0 757 197" aria-hidden="true">
    <path d="M0 22 C60 5 110 8 170 25 S290 45 360 20 S500 0 600 18 S720 30 757 15 V197 H0Z" fill="#1c8fd6" opacity=".55"/>
    <path d="M0 40 C70 20 130 25 190 42 S300 55 380 38 S520 20 620 35 S730 45 757 30 V197 H0Z" fill="#ffffff"/>
  </svg>

  <div class="abs thumb thumb-1" role="img" aria-label="Pool skimmer net lifting leaves from clear water"></div>
  <div class="abs thumb thumb-2" role="img" aria-label="Technicians cleaning a backyard pool"></div>
  <div class="abs thumb thumb-3" role="img" aria-label="Technician repairing pool equipment at the pool edge"></div>

  <div class="abs badge">
    <div class="badge-text"><b>FREE</b><span>27 POINT</span><span>INSPECTION</span></div>
  </div>

  <p class="abs call-line front-call">Call us for <strong>FREE ESTIMATES</strong></p>
  <p class="abs phone front-phone">561-555-0148</p>
  <p class="abs web front-web">www.tidewellservice.com</p>
  <p class="abs social front-social">www.friendnet.com/TidewellFla</p>

  <p class="abs promise-band">We Are Professional <strong>– Provide&nbsp; Fast Reliable Service and Repairs</strong></p>
  <svg class="abs band-slash" width="20" height="20" viewBox="0 0 20 20" aria-hidden="true">
    <path d="M0 0H7L18 20H11Z" fill="#f5a623"/>
  </svg>

  <div class="abs brandmark front-brand"><span class="dot"></span><span class="name">Tidewell</span></div>
</section>

<section class="card card--back">
  <div class="abs brandmark back-brand"><span class="dot"></span><span class="name">Tidewell</span></div>

  <p class="abs back-tagline">We Are Professional<br><strong>Provide&nbsp; Fast Reliable<br>Service and Repairs</strong></p>

  <div class="abs indicia">PRSRT STD<br>ECRWSS<br>U.S. POSTAGE<br>PAID<br>SWPD RETAIL</div>
  <div class="abs address">Local<br>Postal Customer</div>

  <h3 class="abs diff-head">THE TIDEWELL DIFFERENCE</h3>
  <p class="abs diff-motto">DO WHAT YOU LOVE, LOVE WHAT YOU DO</p>

  <ul class="abs diff-list diff-a">
    <li class="bullet">Customers receive e-mails of weekly Pool Service<br>details including PICTURES of your pool</li>
    <li class="bullet">All Pool Service Data is Stored Electronically</li>
    <li class="bullet">Our computer systems and operating procedures<br>enable service consistency</li>
    <li class="bullet">All Employees are CPO’s (Certified Pool Operators)</li>
    <li class="bullet">All Staff wear a Tidewell uniform for you security</li>
  </ul>
  <ul class="abs diff-list diff-b">
    <li class="bullet">All Vehicles have TIDEWELL Name Displayed</li>
    <li>Criminal background checks of all employees</li>
    <li class="bullet">GPS tracking on our trucks for Timely Service</li>
    <li class="bullet">You Speak with our Friendly Customer Service Staff</li>
    <li class="bullet">Great Customer Service on Time, Every Time!</li>
    <li class="bullet">Technicians receive extensive<br>ongoing training</li>
  </ul>

  <svg class="abs back-wave" width="757" height="185" viewBox="0 0 757 185" aria-hidden="true">
    <path d="M0 10 C50 -2 90 2 140 14 S230 28 290 10 S400 -4 470 12 S600 26 680 10 S740 4 757 8 V185 H0Z" fill="#2aa0e0"/>
    <path d="M0 30 C60 14 120 18 180 32 S300 44 370 26 S500 12 580 28 S700 40 757 26 V185 H0Z" fill="#6fcdf5"/>
  </svg>

  <div class="abs round-photo" role="img" aria-label="Technician cleaning a blue tiled pool with a long-handled brush, seen from above"></div>

  <p class="abs ready">READY FOR A CHANGE?</p>
  <p class="abs look">We look forward to working with you!</p>

  <svg class="abs ribbon" width="181" height="54" viewBox="0 0 181 54" aria-hidden="true">
    <path d="M0 0H181V46L90 40L0 46Z" fill="#f5a623"/>
    <path d="M0 46L90 40L181 46V52L90 46L0 52Z" fill="#1b3a8a"/>
  </svg>
  <p class="abs ribbon-text">New Customers<br>Get One Month FREE</p>

  <p class="abs call-line back-call">Call us for <strong>FREE ESTIMATES</strong></p>
  <p class="abs phone back-phone">561-555-0148</p>
  <p class="abs web back-web">www.tidewellservice.com</p>
  <p class="abs social back-social">www.friendnet.com/TidewellFla</p>

  <p class="abs licensed">WE ARE LICENSED AND INSURED</p>
</section>

</body>
</html>
```